Crazy, Different WOMENS PREWORKOUT Packaging Label

We need a MODERN, CRAZY, FUN packaging preworkout label for WOMEN.
There are no limits for this project, be wild and crazy and DIFFERENT.

The name of the product is CALDERA BLUSH and it is a gym preworkout supplement for women.
The company is called VORTANUTRA.

We're looking to convey strength, femininity, uniqueness, health, vitality, vigor, focus, concentration, energy, stamina.

and above all HEALTH
Updates

Project Deadline Extended Reason: Hello All, thanks for your submissions so far. In the interest of receiving the best designs, we will extend the deadline by 5 days. We appreciate your effort and look forward to further revisions to hone and perfect the concepts already submitted. Thank you all for your effort so far! Added Saturday, January 7, 2017

Target Market(s)

Sports Women and Women Gym goers

Font styles to use
Serif
Sans Serif
Decorative
Other font styles liked:
• AR Destine

Requirements
Must have
• It must have SOME red in it somewhere because the product is called CALDERA BLUSH but it does NOT have to be the dominating color.
• It must include our Company logo on the label too, but the company logo and the product name should be harmonious. It should be obvious which part of the design is the company logo and which part is the name of the product.
• Include any one of the Company Logo Strips on the label (see reference files) can make it any color!
Nice to have
• Nice to have something unique and different but appealing to women. but NOT stereotypical of women...
• It should be something strong, elite and feminine BUT NOT bubblegum pink and rainbows...
• The jar is a round white jar.
• Try make it look clean, healthful, effective.
• I'm open to crazy and simple designs.
Should not have
• Should not JUST be pink and purple and stereotypical to women.
• It CAN have pink and purple in it though.

```html
<!DOCTYPE html>
<html lang="en">
<head>
<meta charset="utf-8">
<title>Caldera Blush Preworkout Label</title>
<link rel="stylesheet" href="https://fonts.googleapis.com/css2?family=Jost:ital,wght@0,300;1,400&family=Audiowide&family=Russo+One&family=Oswald:wght@400&display=swap">
<style>
  :root {
    --label-grey: #9a9a9a;
    --label-white: #f3f5f5;
    --label-blush: #c9b0a8;
    --label-brown: #7a3520;
    --label-salmon: #e0705a;
    --label-red-deep: #7e1406;
    --stripe-pink: #ff7aa0;
    --stripe-rose: #c4455a;
    --arrow-lime: #b6ff70;
    --arrow-green: #4a8a00;
    --title-black: #111111;
    --title-red: #e00000;
    --brand-ink: #2a0a3a;
    --brand-dot: #d63c8c;
    --claim-magenta: #ff4fd0;
    --tag-black: #1a0a06;
    --tag-white: #ffffff;
    --leaf-tint: #d9ecc8;
  }
  html, body {
    margin: 0;
    padding: 0;
    width: 1200px;
    height: 905px;
    overflow: hidden;
    background: #ffffff;
  }
  .label {
    position: relative;
    width: 1200px;
    height: 905px;
    overflow: hidden;
  }
  .label-art {
    position: absolute;
    inset: 0;
    width: 1200px;
    height: 905px;
  }
  .product-name {
    position: absolute;
    left: 104px;
    top: 96px;
    margin: 0;
    font-weight: normal;
  }
  .product-name__first {
    display: block;
    font-family: "Jost", sans-serif;
    font-weight: 300;
    font-size: 124px;
    line-height: 1;
    letter-spacing: 2px;
    color: var(--title-black);
  }
  .product-name__second {
    display: block;
    margin-top: 26px;
    margin-left: -8px;
    font-family: "Audiowide", sans-serif;
    font-size: 128px;
    line-height: 1;
    color: var(--title-red);
    transform: skewX(-14deg);
    transform-origin: left bottom;
  }
  .brand {
    position: absolute;
    left: 220px;
    top: 470px;
    display: flex;
    align-items: center;
    gap: 18px;
  }
  .brand__mark {
    width: 30px;
    height: 30px;
    background: var(--brand-dot);
  }
  .brand__name {
    font-family: "Russo One", sans-serif;
    font-size: 70px;
    line-height: 1;
    color: var(--brand-ink);
    letter-spacing: 1px;
  }
  .claim {
    position: absolute;
    right: 640px;
    top: 660px;
    margin: 0;
    font-family: "Oswald", sans-serif;
    font-size: 54px;
    line-height: 52px;
    text-align: right;
    color: var(--claim-magenta);
    text-transform: uppercase;
  }
  .tea-icon {
    position: absolute;
    left: 900px;
    top: 596px;
    width: 176px;
    height: 136px;
    background: var(--leaf-tint);
    border-radius: 50% 10% 50% 10%;
    opacity: 0.85;
  }
  .tea-tag {
    position: absolute;
    left: 812px;
    top: 752px;
    width: 282px;
    height: 38px;
    background: var(--tag-black);
    transform: skewX(-14deg);
    display: flex;
    align-items: center;
    justify-content: center;
  }
  .tea-tag__text {
    font-family: "Jost", sans-serif;
    font-style: italic;
    font-weight: 400;
    font-size: 26px;
    letter-spacing: 2px;
    color: var(--tag-white);
  }
</style>
</head>
<body>
<main class="label">
  <svg class="label-art" viewBox="430 378 620 507" preserveAspectRatio="none" aria-hidden="true">
    <defs>
      <linearGradient id="label-base" x1="430" y1="0" x2="1050" y2="0" gradientUnits="userSpaceOnUse">
        <stop offset="0" stop-color="#9a9a9a"/>
        <stop offset="0.1" stop-color="#dfe2e2"/>
        <stop offset="0.28" stop-color="#f3f5f5"/>
        <stop offset="0.36" stop-color="#c9b0a8"/>
        <stop offset="0.52" stop-color="#7a3520"/>
        <stop offset="0.6" stop-color="#c0573e"/>
        <stop offset="0.78" stop-color="#9a2a12"/>
        <stop offset="0.92" stop-color="#7e1406"/>
        <stop offset="1" stop-color="#9b2a18"/>
      </linearGradient>
      <linearGradient id="pink-stripe" x1="0" y1="378" x2="0" y2="700" gradientUnits="userSpaceOnUse">
        <stop offset="0" stop-color="#ff7aa0"/>
        <stop offset="0.6" stop-color="#f36a96"/>
        <stop offset="1" stop-color="#c4455a"/>
      </linearGradient>
      <linearGradient id="arrow-fill" x1="925" y1="403" x2="800" y2="890" gradientUnits="userSpaceOnUse">
        <stop offset="0" stop-color="#b6ff70"/>
        <stop offset="0.35" stop-color="#4a8a00"/>
        <stop offset="0.7" stop-color="#5a9a10"/>
        <stop offset="1" stop-color="#7fc43a"/>
      </linearGradient>
    </defs>
    <rect class="label-base" x="430" y="378" width="620" height="507" fill="url(#label-base)"/>
    <rect class="pink-stripe" x="808" y="378" width="77" height="320" fill="url(#pink-stripe)"/>
    <polygon class="salmon-band" points="885,378 935,378 1000,440 1000,800 700,800 700,700 885,700" fill="#e0705a"/>
    <polygon class="green-arrow" points="925,403 1050,528 1050,615 1000,570 1000,795 785,795 875,890 780,890 603,718 925,718" fill="url(#arrow-fill)"/>
  </svg>

  <h1 class="product-name">
    <span class="product-name__first">CALDERA</span>
    <span class="product-name__second">BLUSH</span>
  </h1>

  <div class="brand">
    <span class="brand__name">VORTANUTRA</span>
    <span class="brand__mark"></span>
  </div>

  <p class="claim">Gym preworkout<br>supplement<br>for women</p>

  <div class="tea-icon" role="img" aria-label="White bush tea leaf sprig illustration"></div>
  <div class="tea-tag"><span class="tea-tag__text">with bush tea</span></div>
</main>
</body>
</html>
```